Vireo M.K. - Diagnostic Ultrasound Flyer

About US
Vireo M.K. is a concierge ultrasound company that provides onsite or offsite diagnostic ultrasounds. We have over 14 years experience in sonography, business management, and customer service. We offer both the physician and patient flexibility, convenience, and access to timely services.

We provide ultrasounds for the following specialties:
Obstetrics/Gynecology
Abdominal
Small Parts
Vascular

Company Features:
1. Onsite or Offsite Scans
2. Images Available Immediately for Referring Physician and Patient
3. Flexible Options for Ultrasound Interpretation/Billing
4. Access to Interpreting Radiologist
5. Final Report Process - 1-2 Business Days/ 1 hour for STAT.
6. PACS Storage with Secure Access.

We need a place to add in our contact information (address, email, website, phone)

We already have a logo and would like to use it ( they are attached). We would the colors to match the logo colors....maybe lighter version of yellow and blue.

```html
<!DOCTYPE html>
<html lang="en">
<head>
<meta charset="utf-8">
<title>Vireo M.K. - Diagnostic Ultrasound Flyer</title>
<link href="https://fonts.googleapis.com/css2?family=Montserrat:wght@400;500;600;700;800&display=swap" rel="stylesheet">
<style>
  :root {
    --blue: #2d309c;
    --blue-soft: #3b3fb0;
    --yellow: #f7c42a;
    --grey-panel: #eeeff2;
    --text-grey: #8a8c94;
    --white: #ffffff;
    --backdrop: #e7e4df;
  }
  * { margin: 0; padding: 0; box-sizing: border-box; }
  html, body { width: 1200px; height: 964px; overflow: hidden; }
  body {
    background: var(--backdrop);
    font-family: "Montserrat", sans-serif;
    position: relative;
  }
  .flyer {
    position: absolute; left: 245px; top: 22px;
    width: 710px; height: 920px;
    background: var(--white);
    overflow: hidden;
    box-shadow: 0 6px 24px rgba(0,0,0,0.12);
  }
  .call-now {
    position: absolute; right: 44px; top: 30px;
    font-weight: 700; line-height: 1.05;
  }
  .call-now .label { color: var(--blue); font-size: 26px; display: block; }
  .call-now .number { color: var(--yellow); font-size: 28px; letter-spacing: 0.5px; }
  .hero-photo {
    position: absolute; left: 0; top: 105px; width: 710px; height: 375px;
    background: linear-gradient(160deg, #f4f6f8 0%, #e3e7ee 40%, #c9cfdc 70%, #b7bdcd 100%);
  }
  .brand {
    position: absolute; left: 40px; top: 150px;
    display: flex; align-items: center; gap: 10px;
  }
  .brand-dot { width: 16px; height: 16px; border-radius: 50%; background: var(--yellow); }
  .brand-name { color: var(--blue); font-weight: 800; font-size: 44px; letter-spacing: 1px; }
  .about {
    position: absolute; left: 0; top: 480px; width: 300px; height: 258px;
    background: var(--grey-panel); padding: 24px 24px 0 34px;
  }
  .section-title { font-weight: 700; font-size: 28px; color: var(--blue); }
  .section-title .accent { color: var(--yellow); }
  .about .rule { width: 200px; height: 1px; background: var(--text-grey); margin: 6px 0 10px; }
  .about p { color: var(--text-grey); font-size: 12.5px; line-height: 1.45; }
  .features {
    position: absolute; left: 300px; top: 440px; width: 410px; height: 270px;
    background: var(--white); padding-top: 14px;
  }
  .features .section-title { padding-left: 24px; font-size: 30px; margin-bottom: 10px; }
  .feature-list { list-style: none; }
  .feature-list li {
    font-size: 13px; font-weight: 500; color: var(--blue);
    padding: 6px 16px 6px 28px; line-height: 1.3;
  }
  .feature-list li.band { background: var(--blue-soft); color: var(--white); }
  .contact {
    position: absolute; left: 330px; top: 728px; width: 380px; height: 76px;
    background: var(--yellow); border-radius: 38px 0 0 38px;
    padding: 12px 0 0 34px;
  }
  .contact h3 { color: var(--blue); font-weight: 700; font-size: 19px; }
  .contact .rule { width: 190px; height: 1px; background: var(--blue); margin: 3px 0 4px; }
  .contact p { color: var(--blue); font-size: 10.5px; line-height: 1.45; }
  .contact b { font-weight: 700; }
  .map-badge {
    position: absolute; left: 592px; top: 690px; width: 104px; height: 104px;
    border-radius: 50%; border: 3px solid var(--white);
    box-shadow: 0 0 0 2px var(--blue);
    background: radial-gradient(circle at 45% 45%, #f3f1ea, #dfe6d9);
  }
  .specialties { position: absolute; left: 44px; top: 754px; width: 250px; }
  .specialties h4 { font-size: 15px; font-weight: 600; color: var(--blue); line-height: 1.2; }
  .specialties h4 .accent { color: var(--yellow); }
  .specialty-list { list-style: none; margin-top: 4px; }
  .specialty-list li { font-size: 13.5px; color: var(--text-grey); line-height: 1.5; display: flex; align-items: center; gap: 6px; }
  .specialty-list svg { width: 11px; height: 11px; flex: none; }
  .website {
    position: absolute; right: 30px; top: 866px;
    color: var(--blue); font-weight: 700; font-size: 17px; letter-spacing: 4px;
  }
  .website .accent { color: var(--yellow); }
  .footer-rule { position: absolute; left: 0; top: 898px; width: 300px; height: 2px; background: var(--blue); }
  .base-rule { position: absolute; left: 0; bottom: 0; width: 710px; height: 4px; background: var(--blue); }
</style>
</head>
<body>
  <main class="flyer">
    <div class="call-now">
      <span class="label">Call now</span>
      <span class="number">012-555-0148</span>
    </div>

    <div class="hero-photo" role="img" aria-label="Photo of a sonographer performing an ultrasound scan on a patient while a nurse looks on, monitor in the background"></div>

    <div class="brand">
      <span class="brand-dot"></span>
      <span class="brand-name">Vireo M.K.</span>
    </div>

    <section class="about">
      <h2 class="section-title">About <span class="accent">US</span></h2>
      <div class="rule"></div>
      <p>Vireo M.K. is a concierge ultrasound company that provides onsite or offsite diagnostic ultrasounds. We have over 14 years experience in sonography, business management, and customer service. We offer both the physician and patient flexibility, convenience, and access to timely services.</p>
    </section>

    <section class="features">
      <h2 class="section-title">Company <span class="accent">Features:</span></h2>
      <ol class="feature-list">
        <li class="band">1. Onsite or Offsite Scans</li>
        <li>2. Images Available Immediately for Referring<br>&nbsp;&nbsp;&nbsp;&nbsp;Physician and Patient</li>
        <li class="band">3. Flexible Options for Ultrasound Interpretation/Billing</li>
        <li>4. Access to Interpreting Radiologist</li>
        <li class="band">5. Final Report Process - 1-2 Business Days/ 1 hour<br>&nbsp;&nbsp;&nbsp;&nbsp;for STAT.</li>
        <li>6. PACS Storage with Secure Access.</li>
      </ol>
    </section>

    <section class="contact">
      <h3>Contact information</h3>
      <div class="rule"></div>
      <p><b>A:</b> #48 Larkfield Road, Westbury, 00417</p>
      <p><b>E:</b> info@vireomkultrasounds.com</p>
    </section>
    <div class="map-badge" role="img" aria-label="Small street map showing the clinic location with a pin"></div>

    <section class="specialties">
      <h4>We provide ultrasounds for<br><span class="accent">The following specialties:</span></h4>
      <ul class="specialty-list">
        <li><svg viewBox="0 0 12 12"><path d="M1 6.5 L4.5 10 L11 2" fill="none" stroke="#2d309c" stroke-width="1.8"/></svg>Obstetrics/Gynecology</li>
        <li><svg viewBox="0 0 12 12"><path d="M1 6.5 L4.5 10 L11 2" fill="none" stroke="#2d309c" stroke-width="1.8"/></svg>Abdominal</li>
        <li><svg viewBox="0 0 12 12"><path d="M1 6.5 L4.5 10 L11 2" fill="none" stroke="#2d309c" stroke-width="1.8"/></svg>Small Parts</li>
        <li><svg viewBox="0 0 12 12"><path d="M1 6.5 L4.5 10 L11 2" fill="none" stroke="#2d309c" stroke-width="1.8"/></svg>Vascular</li>
      </ul>
    </section>

    <div class="website">www.<span class="accent">vireomkultrasounds</span>.com</div>
    <div class="footer-rule"></div>
    <div class="base-rule"></div>
  </main>
</body>
</html>
```